First Reponders Promotion poster/flyer

Our Yoga studio is introducing an ongoing promotion for all First Responders, Police/Nurse/Paramedic/Firefighters/Doctors
$22pw for Unlimited access to our Inner city Studio which will become a sanctuary for the people who look after us. Tag line: You look after us, let us look after you. The benefits of yoga, reduce stress, clear mind, healthy body. Feel free to use other assets, and be as creative as you like I have just put images and designs as a guide.

Target Market(s)

Emergency Services Tasmania

Industry/Entity Type

Emergency Services

Requirements
Must have
• Stillwave Logo/Address 41 Marlow St/ website www.stillwavestudio.com.a/ sign up online and just bring in current work Id at checkin/$22pw Unlimited classes/Australian market so can't look like usa or any other countries
Nice to have
• words , inner city Sanctuary
Should not have
• Foreign Country images

```html
<!DOCTYPE html>
<html lang="en">
<head>
<meta charset="utf-8">
<title>Stillwave – First Responders Promo</title>
<link href="https://fonts.googleapis.com/css2?family=Roboto+Condensed:ital,wght@0,300;0,400;0,700;1,700&family=Roboto:wght@900&display=swap" rel="stylesheet">
<style>
  :root {
    --gold: #d08a2e;
    --ink: #111111;
    --paper: #ffffff;
    --backdrop: #e8e8e8;
  }
  html, body {
    margin: 0;
    padding: 0;
    width: 1200px;
    height: 1200px;
    overflow: hidden;
    background: var(--backdrop);
  }
  .poster {
    position: absolute;
    left: 196px;
    top: 30px;
    width: 807px;
    height: 1140px;
    background: var(--paper);
    overflow: hidden;
    font-family: "Roboto Condensed", "Arial Narrow", sans-serif;
    color: var(--ink);
  }
  .photo-grid {
    position: absolute;
    left: 0;
    top: 0;
    width: 807px;
    height: 1140px;
  }
  .headline {
    position: absolute;
    left: 52px;
    top: 38px;
    margin: 0;
    font-weight: 700;
    font-size: 89px;
    line-height: 1;
    color: var(--gold);
    letter-spacing: 0.5px;
    white-space: nowrap;
  }
  .headline-sub {
    position: absolute;
    right: 44px;
    top: 130px;
    font-family: "Roboto", Arial, sans-serif;
    font-weight: 900;
    font-size: 39px;
    line-height: 1;
    letter-spacing: 17px;
    margin-right: -17px;
  }
  .tagline {
    position: absolute;
    left: 53px;
    top: 150px;
    margin: 0;
    line-height: 1.12;
  }
  .tagline-soft {
    display: block;
    font-weight: 300;
    font-size: 43px;
  }
  .tagline-strong {
    display: block;
    font-weight: 700;
    font-style: italic;
    font-size: 45px;
  }
  .intro {
    position: absolute;
    left: 51px;
    top: 283px;
    margin: 0;
    font-size: 22px;
    line-height: 28.6px;
  }
  .intro strong { font-weight: 700; }
  .roles {
    position: absolute;
    left: 51px;
    top: 396px;
    margin: 0;
    padding: 0;
    list-style: none;
    font-size: 22px;
    line-height: 27.8px;
  }
  .roles li {
    position: relative;
    padding-left: 24px;
  }
  .roles li::before {
    content: "";
    position: absolute;
    left: 6px;
    top: 9px;
    width: 11px;
    height: 11px;
    border-radius: 50%;
    background: var(--gold);
  }
  .price {
    position: absolute;
    left: 50px;
    top: 633px;
    font-weight: 700;
    font-size: 58px;
    line-height: 1;
    color: var(--gold);
  }
  .offer {
    position: absolute;
    left: 51px;
    top: 699px;
    margin: 0;
    font-size: 22px;
    line-height: 27.8px;
    width: 420px;
  }
  .benefits {
    position: absolute;
    left: 51px;
    top: 828px;
    margin: 0;
    font-weight: 700;
    font-style: italic;
    font-size: 29px;
    line-height: 37px;
  }
  .benefits-lead { display: block; color: var(--gold); }
  .benefits-list { display: block; }
  .brand-name {
    position: absolute;
    left: 52px;
    top: 944px;
    font-weight: 700;
    font-size: 38px;
    line-height: 1;
    letter-spacing: 14px;
    color: var(--ink);
  }
  .contact-divider {
    position: absolute;
    left: 406px;
    top: 946px;
    width: 3px;
    height: 121px;
    background: var(--gold);
  }
  .contact {
    position: absolute;
    left: 431px;
    top: 944px;
    width: 360px;
  }
  .contact-line {
    display: flex;
    align-items: center;
    gap: 6px;
    font-size: 22px;
    line-height: 28px;
  }
  .contact-line svg { width: 17px; height: 17px; flex: none; }
  .signup {
    margin-top: 4px;
    font-weight: 700;
    font-size: 38px;
    line-height: 1.05;
    color: var(--gold);
  }
  .checkin {
    margin-top: 2px;
    font-size: 19px;
    line-height: 1.1;
    white-space: nowrap;
  }
  .checkin .lead { font-size: 22px; }
  .checkin strong { font-weight: 700; }
  .footer-band {
    position: absolute;
    left: 0;
    bottom: 0;
    width: 807px;
    height: 45px;
    background: var(--gold);
  }
</style>
</head>
<body>
<main class="poster">

  <svg class="photo-grid" viewBox="0 0 1128 1594" preserveAspectRatio="none">
    <defs>
      <linearGradient id="tone-nurse" x1="0" y1="0" x2="0" y2="1">
        <stop offset="0" stop-color="#e6e6e4"/>
        <stop offset="0.55" stop-color="#c9cdca"/>
        <stop offset="1" stop-color="#7f978f"/>
      </linearGradient>
      <linearGradient id="tone-patrol" x1="0" y1="0" x2="1" y2="1">
        <stop offset="0" stop-color="#1c1d20"/>
        <stop offset="0.5" stop-color="#3b3e44"/>
        <stop offset="1" stop-color="#0e0f11"/>
      </linearGradient>
      <linearGradient id="tone-ambulance" x1="0" y1="0" x2="0" y2="1">
        <stop offset="0" stop-color="#8e9496"/>
        <stop offset="0.5" stop-color="#b8aea0"/>
        <stop offset="1" stop-color="#5b5650"/>
      </linearGradient>
      <linearGradient id="tone-vest" x1="0" y1="0" x2="1" y2="1">
        <stop offset="0" stop-color="#2a3546"/>
        <stop offset="0.35" stop-color="#3f6f9a"/>
        <stop offset="0.6" stop-color="#c6d94a"/>
        <stop offset="1" stop-color="#a5b83a"/>
      </linearGradient>
      <linearGradient id="tone-fire" x1="0" y1="0" x2="1" y2="1">
        <stop offset="0" stop-color="#c8b48a"/>
        <stop offset="0.45" stop-color="#e3d24a"/>
        <stop offset="0.75" stop-color="#7d6a4c"/>
        <stop offset="1" stop-color="#4a3f33"/>
      </linearGradient>
    </defs>
    <polygon role="img" aria-label="Photo: nurse in scrubs with stethoscope" fill="url(#tone-nurse)" points="695,257 897,461 695,662 490,461"/>
    <polygon role="img" aria-label="Photo: police officers seated in a patrol car" fill="url(#tone-patrol)" points="485,470 690,674 485,877 278,674"/>
    <polygon role="img" aria-label="Photo: smiling paramedics inside an ambulance" fill="url(#tone-ambulance)" points="695,682 897,884 695,1087 490,884"/>
    <polygon role="img" aria-label="Photo: police officer in high-visibility vest" fill="url(#tone-vest)" points="712,670 1098,284 1128,314 1128,1100 906,892"/>
    <polygon role="img" aria-label="Photo: firefighter in helmet and breathing mask" fill="url(#tone-fire)" points="705,1092 908,892 1128,1112 1128,1410 1068,1470"/>
  </svg>

  <h1 class="headline">FIRST RESPONDERS</h1>
  <div class="headline-sub">PROMO</div>

  <p class="tagline">
    <span class="tagline-soft">You look after us,</span>
    <span class="tagline-strong">let us look after you!</span>
  </p>

  <p class="intro">Our Yoga studio is introducing<br>an ongoing promotion for all<br><strong>First Responders</strong></p>

  <ul class="roles">
    <li>Paramedic</li>
    <li>Ambulance</li>
    <li>Nurse</li>
    <li>Police</li>
    <li>Firefighters</li>
    <li>SES</li>
    <li>Doctors</li>
  </ul>

  <div class="price">$22pw</div>
  <p class="offer">for Unlimited access to our Inner<br>city Studio which will become a<br>sanctuary for the people who look after us.</p>

  <p class="benefits">
    <span class="benefits-lead">The benefits of yoga,</span>
    <span class="benefits-list">reduce stress, clear mind, healthy body.</span>
  </p>

  <div class="brand-name">STILLWAVE</div>

  <div class="contact-divider"></div>
  <div class="contact">
    <div class="contact-line">
      <svg viewBox="0 0 24 24" aria-hidden="true"><path d="M12 2a7 7 0 0 0-7 7c0 5 7 13 7 13s7-8 7-13a7 7 0 0 0-7-7zm0 9.5A2.5 2.5 0 1 1 12 6.5a2.5 2.5 0 0 1 0 5z" fill="var(--gold)"/></svg>
      <span>41 Marlow St</span>
    </div>
    <div class="contact-line">
      <svg viewBox="0 0 24 24" aria-hidden="true" fill="none" stroke="var(--gold)" stroke-width="1.6"><circle cx="12" cy="12" r="9"/><ellipse cx="12" cy="12" rx="4" ry="9"/><line x1="3" y1="12" x2="21" y2="12"/><line x1="4.5" y1="7.5" x2="19.5" y2="7.5"/><line x1="4.5" y1="16.5" x2="19.5" y2="16.5"/></svg>
      <span>www.stillwavestudio.com</span>
    </div>
    <div class="signup">SIGN UP ONLINE</div>
    <div class="checkin"><span class="lead">and</span> just bring in current <strong>work Id</strong> at checkin</div>
  </div>

  <div class="footer-band"></div>
</main>
</body>
</html>
```